Brennick Drilling Inc. Business card design

Business card design for "Brennick Drilling Inc. - Directional Drilling Services"

Address is:

Brennick Drilling Inc.
512 - 73 Tarvel Crescent SW
Calgary, Alberta, Canada
T2K 4P8

Please incorporate the logo design into the card, thank you.

Target Market(s)

Oil & Gas and Drilling

Industry/Entity Type

Business

```html
<!DOCTYPE html>
<html lang="en">
<head>
<meta charset="utf-8">
<title>Brennick Drilling Inc. – Business Card</title>
<link href="https://fonts.googleapis.com/css2?family=Open+Sans:wght@400;700&display=swap" rel="stylesheet">
<style>
  :root {
    --backdrop: #cfcfcf;
    --card: #ffffff;
    --ink: #1c1c1c;
    --text-grey: #4a4a4a;
    --brand-red: #e0402f;
  }
  html, body {
    margin: 0;
    width: 1200px;
    height: 1001px;
    overflow: hidden;
    background: var(--backdrop);
    font-family: "Open Sans", Arial, sans-serif;
  }
  .sheet {
    position: relative;
    width: 1200px;
    height: 1001px;
  }
  .card {
    position: absolute;
    width: 525px;
    height: 300px;
    background: var(--card);
    box-shadow: 0 6px 18px rgba(0,0,0,0.18);
    box-sizing: border-box;
  }
  .card--front { left: 80px; top: 150px; }
  .card--back  { left: 595px; top: 551px; }

  .brand {
    display: flex;
    align-items: center;
    gap: 12px;
  }
  .brand__dot {
    width: 34px;
    height: 34px;
    border-radius: 50%;
    background: var(--ink);
    flex: none;
  }
  .brand__name {
    font-weight: 700;
    font-size: 22px;
    color: var(--ink);
    letter-spacing: 0.5px;
    white-space: nowrap;
  }

  .card--front .brand {
    position: absolute;
    left: 50%;
    top: 50%;
    transform: translate(-50%, -50%);
  }

  .card--back .brand {
    position: absolute;
    left: 34px;
    top: 40px;
  }

  .address {
    position: absolute;
    right: 40px;
    bottom: 48px;
    margin: 0;
    font-style: normal;
    font-size: 15px;
    line-height: 1.45;
    color: var(--text-grey);
  }
  .address__company {
    color: var(--brand-red);
  }
</style>
</head>
<body>
<main class="sheet">
  <section class="card card--front" aria-label="Card front">
    <div class="brand">
      <span class="brand__dot"></span>
      <span class="brand__name">Brennick Drilling Inc.</span>
    </div>
  </section>

  <section class="card card--back" aria-label="Card back">
    <div class="brand">
      <span class="brand__dot"></span>
      <span class="brand__name">Brennick Drilling Inc.</span>
    </div>
    <address class="address">
      <span class="address__company">Brennick Drilling Inc.</span><br>
      512 - 73 Tarvel Crescent SW<br>
      Calgary, Alberta, Canada<br>
      T2K 4P8
    </address>
  </section>
</main>
</body>
</html>
```